Professional Photography Business cards

I need business cards that include my logo which I have uploaded. I run a photography business. I am open to ideas but I would like one side to have my logo and the other side to have my contact info. I don't have a website made but I do own a website domain. I have uploaded 2 different logo color schemes. My business colors are Blue, black , and white.

Business Name
Business Phone Number
Business Email
Business Website address
Instagram

Industry/Entity Type

Professional Photography

Contact Information for Business Card

Phone Number: 555-304-7826 email: info@tkale-studio.example Instagram: @t.kalestudio website doman- www.tkale-studio.example

Requirements
Must have
• I like the idea of a business card with a full black background front and back of card. My colors must include royal blue, black, and white

```html
<!DOCTYPE html>
<html lang="en">
<head>
<meta charset="UTF-8">
<title>Tessa Kale – Business Card</title>
<link href="https://fonts.googleapis.com/css2?family=Roboto:wght@400;500&display=swap" rel="stylesheet">
<style>
  :root {
    --backdrop: #cbcbcb;
    --card-navy: #1a1c38;
    --ink-white: #f2f2f4;
    --ink-soft: #d9dae2;
    --icon-line: #b9bbc9;
  }
  * { margin: 0; padding: 0; box-sizing: border-box; }
  html, body {
    width: 1200px; height: 820px; overflow: hidden;
    background: var(--backdrop);
    font-family: "Roboto", Arial, sans-serif;
  }
  .stage { position: relative; width: 1200px; height: 820px; }
  .card {
    position: absolute; top: 127px;
    width: 322px; height: 565px;
    background: var(--card-navy);
    color: var(--ink-white);
    overflow: hidden;
  }
  .card--front { left: 242px; }
  .card--back { left: 636px; }

  .brand {
    position: absolute; left: 0; width: 100%;
    display: flex; align-items: center; justify-content: center; gap: 10px;
  }
  .card--front .brand { top: 144px; }
  .card--back .brand { top: 452px; }
  .brand__name {
    font-size: 26px; font-weight: 400; letter-spacing: 1px;
    color: var(--ink-white);
  }
  .brand__mark {
    width: 30px; height: 30px; border-radius: 50%;
    border: 2px solid var(--ink-white);
  }

  .identity { position: absolute; top: 314px; width: 100%; text-align: center; }
  .identity__name {
    font-size: 20px; font-weight: 500; letter-spacing: 2px;
    color: var(--ink-soft);
  }
  .identity__role {
    margin-top: 3px; font-size: 11px; letter-spacing: 1.5px;
    color: var(--ink-soft);
  }

  .icon-row {
    position: absolute; top: 375px; width: 100%;
    display: flex; justify-content: center; gap: 10px;
  }
  .icon-row svg { width: 14px; height: 14px; }

  .contact-list {
    position: absolute; top: 412px; width: 100%;
    list-style: none; text-align: center;
    font-size: 12px; letter-spacing: 0.8px; color: var(--ink-soft);
  }
  .contact-list li { height: 25px; line-height: 16px; }
  .contact-list strong { font-weight: 500; color: var(--ink-white); }

  .closing-dash {
    position: absolute; top: 521px; left: 150px;
    width: 12px; height: 2px; background: var(--ink-white);
  }

  .hang-line {
    position: absolute; left: 156px; top: 0;
    width: 2px; height: 92px; background: var(--ink-white);
  }
  .vertical-url {
    position: absolute; left: 148px; top: 107px; height: 238px;
    writing-mode: vertical-rl; transform: rotate(180deg);
    font-size: 13px; letter-spacing: 1.2px; color: var(--ink-white);
    text-align: left;
  }
  .vertical-url strong { font-weight: 500; }
</style>
</head>
<body>
<main class="stage">
  <section class="card card--front" aria-label="Card front with contact details">
    <div class="brand">
      <span class="brand__name">T. Kale Studio</span>
      <span class="brand__mark"></span>
    </div>

    <div class="identity">
      <h1 class="identity__name">TESSA KALE</h1>
      <p class="identity__role">PHOTOGRAPHER</p>
    </div>

    <div class="icon-row" aria-hidden="true">
      <svg viewBox="0 0 14 14" fill="none" stroke="var(--icon-line)" stroke-width="0.9">
        <circle cx="7" cy="7" r="6.4"/>
        <path d="M4.6 4.2c.4-.4.8-.4 1 0l.6 1c.2.3 0 .6-.2.8l-.3.3c.3.8.9 1.4 1.7 1.8l.3-.3c.2-.2.5-.3.8-.1l1 .6c.4.2.4.6 0 1l-.5.5c-1.8.4-4.8-2.6-4.6-4.5z"/>
      </svg>
      <svg viewBox="0 0 14 14" fill="none" stroke="var(--icon-line)" stroke-width="0.9">
        <circle cx="7" cy="7" r="6.4"/>
        <rect x="3.8" y="4.8" width="6.4" height="4.4"/>
        <path d="M3.8 4.8 7 7.4l3.2-2.6"/>
      </svg>
      <svg viewBox="0 0 14 14" fill="none" stroke="var(--icon-line)" stroke-width="0.9">
        <circle cx="7" cy="7" r="6.4"/>
        <circle cx="7" cy="7" r="3.4"/>
        <path d="M3.6 7h6.8M7 3.6c-1.4 1.8-1.4 5 0 6.8M7 3.6c1.4 1.8 1.4 5 0 6.8"/>
      </svg>
      <svg viewBox="0 0 14 14" fill="none" stroke="var(--icon-line)" stroke-width="0.9">
        <circle cx="7" cy="7" r="6.4"/>
      </svg>
    </div>

    <ul class="contact-list">
      <li>555-304-7826</li>
      <li>info@tkale-studio.example</li>
      <li>www.<strong>tkale-studio</strong>.example</li>
      <li>@t.kalestudio</li>
    </ul>

    <span class="closing-dash"></span>
  </section>

  <section class="card card--back" aria-label="Card back with brand name">
    <span class="hang-line"></span>
    <p class="vertical-url">www.<strong>tkale-studio</strong>.example</p>
    <div class="brand">
      <span class="brand__name">T. Kale Studio</span>
      <span class="brand__mark"></span>
    </div>
  </section>
</main>
</body>
</html>
```